Exceptional Properties Flyer

I need a flyer template that I can re-use for high-end home listings over $1m in price. 11 X 17 horizontal folded to open wtih front photo shot large on front with short descriptionon areas, room for my photo, logo, contact info & property address then photo slots inside all pagers with room for copy to be plugged in. 3-4 photo spots per page at various sizes but room for bullet point descriptions on pages somewhere. Back of flyer larger photo slot and 2-3 smaller spots below with room for my photo and contact info
My contact info:
Lydia Fenwick
Real Estate Broker
Harlow Crest Real Estate
Direct 555.014.7382
Email: lydia.fenwic@oakmerehomes.com

```html
<!DOCTYPE html>
<html lang="en">
<head>
<meta charset="utf-8">
<title>Exceptional Properties Flyer</title>
<link href="https://fonts.googleapis.com/css2?family=Raleway:ital,wght@0,400;0,500;0,600;0,700;0,800;1,500&display=swap" rel="stylesheet">
<style>
:root{
  --stage:#4b4b4d;
  --paper:#ffffff;
  --ink:#111111;
  --black:#050505;
  --grey:#8a8a8a;
  --grey-light:#bdbdbd;
  --grey-dark:#5e5e5e;
  --text:#2a2a2a;
  --font:'Raleway', Arial, sans-serif;
}
*{margin:0;padding:0;box-sizing:border-box}
html,body{width:1200px;height:1200px;overflow:hidden}
body{background:radial-gradient(circle at 50% 40%,#58585a,var(--stage) 70%);font-family:var(--font);color:var(--ink);position:relative}
.page{position:absolute;background:var(--paper);overflow:hidden}
.cover{left:176px;top:70px;width:406px;height:526px}
.front{left:582px;top:70px;width:408px;height:526px;border-left:1px solid #ddd}
.inside-left{left:176px;top:596px;width:406px;height:530px;border-top:2px solid #444}
.inside-right{left:582px;top:596px;width:408px;height:530px;border-top:2px solid #444;border-left:1px solid #ddd}
.abs{position:absolute}
.photo{position:absolute}
.photo.kitchen{background:linear-gradient(160deg,#e9e1d6 0%,#d8c6ae 45%,#b89f82 100%)}
.photo.living{background:linear-gradient(160deg,#efe9df 0%,#cdbfa6 55%,#a68e6c 100%)}
.photo.bath{background:linear-gradient(160deg,#8a5a30 0%,#c08a52 50%,#5a3518 100%)}
.photo.house{background:linear-gradient(180deg,#8fb8de 0%,#c9d7e2 28%,#d9cf8a 50%,#6b7f4a 80%,#3d5a2a 100%)}
.photo.lounge{background:linear-gradient(165deg,#e9e2cf 0%,#c9b57a 50%,#8e7a4c 100%)}
.photo.agent{background:linear-gradient(180deg,#9fb4c6 0%,#d8c08a 45%,#2a2a30 100%);border:2px solid #fff}
.logo{position:absolute;text-align:center;color:var(--ink);white-space:nowrap}
.logo .name{font-weight:800;font-size:17px;letter-spacing:-.3px;line-height:1}
.logo .tag{font-weight:600;font-size:8.5px;letter-spacing:1px;text-transform:uppercase;margin-top:5px;line-height:1}
.band{position:absolute;left:0;top:366px;width:100%;height:160px;background:var(--black)}
.web{position:absolute;left:0;top:366px;width:100%;text-align:center;color:#f1f1f1;font-size:13px;line-height:22px;font-weight:500;padding-left:50px}
.contact-cover{position:absolute;left:136px;top:408px;color:#fff}
.contact-cover .firm{font-weight:700;font-size:17px}
.contact-cover .who{font-weight:600;font-size:20px;color:var(--grey-light);margin-top:4px}
.contact-cover .role{font-style:italic;font-weight:500;font-size:11px}
.contact-cover .phone{font-weight:700;font-size:20px;margin-top:5px}
.contact-cover .mail{font-size:11px;font-weight:500}
.address-bar{position:absolute;left:0;top:366px;width:100%;height:27px;background:linear-gradient(90deg,#777,#9a9a9a);color:#fff;font-weight:700;font-size:14px;line-height:27px;padding-left:19px}
.desc{position:absolute;left:19px;top:408px;width:215px}
.desc h2{font-weight:800;font-size:17px}
.desc p{font-size:10px;line-height:12px;color:var(--text);margin-top:3px}
.contact-front{position:absolute;right:24px;top:440px;text-align:right}
.contact-front .who{font-weight:700;font-size:16px}
.contact-front .role{font-style:italic;font-weight:500;font-size:9px}
.contact-front .phone{font-weight:800;font-size:20px;margin-top:2px}
.contact-front .mail{font-size:9px}
.page-head{position:absolute;left:24px;top:36px;font-weight:800;font-size:27px}
.intro{position:absolute;left:24px;top:72px;width:370px;font-size:9.6px;line-height:13.5px;color:var(--text)}
.caption-bar{position:absolute;left:24px;top:288px;width:365px;height:58px;background:linear-gradient(90deg,#6f6f6f,#a9a9a9);color:#fff;padding:6px 10px}
.caption-bar h3{font-weight:600;font-size:14px}
.caption-bar p{font-size:9px;line-height:11px;margin-top:1px}
.column{position:absolute;top:356px;width:171px;font-size:7px;line-height:10.6px;text-align:justify;color:var(--text)}
.subhead{position:absolute;left:18px;width:236px}
.subhead h4{font-weight:700;font-size:10px}
.subhead p{font-size:5.5px;line-height:7.5px;color:var(--text)}
.bullets-panel{position:absolute;left:259px;top:100px;width:149px;height:430px;background:var(--black);color:#fff;padding:52px 6px 0 10px}
.bullets-panel h2{font-weight:600;font-size:16px;line-height:18px;color:#c8c8c8}
.bullets-panel ul{list-style:none;margin-top:7px}
.bullets-panel li{position:relative;padding-left:12px;font-weight:700;font-size:11px;line-height:13px;margin-bottom:6px}
.bullets-panel li::before{content:"";position:absolute;left:1px;top:5px;width:3px;height:3px;border-radius:50%;background:#fff}
</style>
</head>
<body>

<!-- Cover page -->
<section class="page cover">
  <div class="photo kitchen" style="left:0;top:0;width:406px;height:268px" role="img" aria-label="Bright modern kitchen with dining table"></div>
  <svg class="abs" style="left:0;top:0" width="406" height="140" viewBox="0 0 406 140">
    <path d="M0 0H290C230 50 140 100 0 102Z" fill="#fff"/>
    <path d="M0 102C140 100 230 50 290 0H300C250 58 150 118 0 122Z" fill="#0a0a0a"/>
    <path d="M0 122C150 118 250 58 300 0H308C260 64 160 126 0 128Z" fill="#d6d6d6"/>
  </svg>
  <div class="logo" style="left:18px;top:30px;width:140px">
    <div class="name">Oakmere Homes</div>
    <div class="tag">Real Estate Center</div>
  </div>
  <div class="photo living" style="left:0;top:268px;width:406px;height:98px" role="img" aria-label="Living room interior"></div>
  <div class="photo bath" style="left:118px;top:268px;width:140px;height:98px" role="img" aria-label="Bathroom vanity with vessel sink"></div>
  <div class="photo lounge" style="left:250px;top:268px;width:156px;height:98px" role="img" aria-label="Sitting room with sofa"></div>
  <svg class="abs" style="left:0;top:268px" width="406" height="98" viewBox="0 0 406 98">
    <polygon points="126,0 132,0 112,98 106,98" fill="#fff"/>
    <polygon points="250,0 256,0 236,98 230,98" fill="#fff"/>
    <rect x="0" y="0" width="406" height="2" fill="#fff"/>
  </svg>
  <div class="band"></div>
  <svg class="abs" style="left:0;top:366px" width="406" height="26" viewBox="0 0 406 26">
    <path d="M128 0H330C320 0 316 24 300 24H170C150 24 144 0 128 0Z" fill="#8a8a8a"/>
  </svg>
  <div class="web">www.oakmerehomes.com</div>
  <div class="photo agent" style="left:24px;top:380px;width:94px;height:121px" role="img" aria-label="Portrait of the listing broker"></div>
  <div class="contact-cover">
    <div class="firm">HARLOW CREST REAL ESTATE</div>
    <div class="who">Lydia Fenwick</div>
    <div class="role">Real Estate Broker</div>
    <div class="phone">555.014.7382</div>
    <div class="mail">lydia.fenwic@oakmerehomes.com</div>
  </div>
</section>

<!-- Front listing page -->
<section class="page front">
  <div class="photo house" style="left:0;top:0;width:408px;height:366px" role="img" aria-label="Exterior of yellow two-storey house with garden"></div>
  <div class="address-bar">PROPERTY ADDRESS WILL GO HERE</div>
  <div class="photo agent" style="left:291px;top:322px;width:93px;height:113px" role="img" aria-label="Portrait of the listing broker"></div>
  <div class="desc">
    <h2>PROPERTY DESCRIPTION</h2>
    <p>Beatur aligniatur aut eos utem hillaut dunducia comnis qui sundeRo odi doluptur? Itatem qui dolut ut ut qui ipsumquati tempori tatiae pre sint velecea simpor</p>
  </div>
  <div class="contact-front">
    <div class="who">Lydia Fenwick</div>
    <div class="role">Real Estate Broker</div>
    <div class="phone">555.014.7382</div>
    <div class="mail">lydia.fenwic@oakmerehomes.com</div>
  </div>
</section>

<!-- Inside left page -->
<section class="page inside-left">
  <h1 class="page-head">PAGE HEAD WILL GO HERE</h1>
  <p class="intro">Beatur aligniatur aut eos utem hillaut dunducia comnis qui sundeRo odi doluptur? Itatem qui dolut ut ut qui ipsumquati tempori tatiae pre sint velecea simpor</p>
  <div class="photo living" style="left:24px;top:108px;width:365px;height:180px" role="img" aria-label="Formal living room with gold drapes"></div>
  <div class="caption-bar">
    <h3>YOUR SUBHEAD WILL GO HERE</h3>
    <p>Beatur aligniatur aut eos utem hillaut dunducia comnis qui sundeRo odi doluptur? Itatem qui dolut ut ut qui ipsumquati tempori tatiae pre sint</p>
  </div>
  <p class="column" style="left:24px">Omniscid ucitassit dolorru mendeni hicidenderum quaepudis receaquiae vel idellup tatquis autem et harit, ut excest, cumqui se preribus rehent aut placcae inis maxima quis nis dolupic turiam aut illendit etur, sit omnis moluptatquam quide et vendigenimi, coribus si dolorit mi, comnimusam rempor aut ate nus, tem ullaut reptas non concer ovition seriate volorrorumet vollabo. Ibus ad maio venduci aut fugit quate volorat mod qui dente es nostrum undam rem que pro ma sum quia soluptate niam et dolorrovid est ad qui consequatur? Agnature et ut vendaer rundaescium re omnieni scitas serio blatiae velibus et endi volorem eost ut vere aliquat explaborem fuga. Et eos esseris</p>
  <p class="column" style="left:218px">Omniscid ucitassit dolorru mendeni hicidenderum quaepudis receaquiae vel idellup tatquis autem et harit, ut excest, cumqui se preribus rehent aut placcae inis maxima quis nis dolupic turiam aut illendit etur, sit omnis moluptatquam quide et vendigenimi, coribus si dolorit mi, comnimusam rempor aut ate nus, tem ullaut reptas non concer ovition seriate volorrorumet vollabo. Ibus ad maio venduci aut fugit quate volorat mod qui dente es nostrum undam rem que pro ma sum quia soluptate niam et dolorrovid est ad qui consequatur? Agnature et ut vendaer rundaescium re omnieni scitas serio blatiae velibus et endi volorem eost ut vere aliquat explaborem fuga. Et eos esseris</p>
</section>

<!-- Inside right page -->
<section class="page inside-right">
  <div class="photo kitchen" style="left:18px;top:26px;width:236px;height:114px" role="img" aria-label="Kitchen with dining table"></div>
  <div class="subhead" style="top:145px">
    <h4>YOUR SUBHEAD WILL GO HERE</h4>
    <p>Beatur aligniatur aut eos utem hillaut dunducia comnis qui sundeRo odi doluptur? Itatem qui dolut ut ut qui ipsumquati tempori tatiae pre sint velecea simpor</p>
  </div>
  <div class="photo lounge" style="left:18px;top:188px;width:236px;height:114px" role="img" aria-label="Living room with fireplace and sofa"></div>
  <div class="subhead" style="top:310px">
    <h4>YOUR SUBHEAD WILL GO HERE</h4>
    <p>Beatur aligniatur aut eos utem hillaut dunducia comnis qui sundeRo odi doluptur? Itatem qui dolut ut ut qui ipsumquati tempori tatiae pre sint velecea simpor</p>
  </div>
  <div class="photo bath" style="left:18px;top:352px;width:236px;height:112px" role="img" aria-label="Bathroom vanity with vessel sink"></div>
  <div class="subhead" style="top:469px">
    <h4>YOUR SUBHEAD WILL GO HERE</h4>
    <p>Beatur aligniatur aut eos utem hillaut dunducia comnis qui sundeRo odi doluptur? Itatem qui dolut ut ut qui ipsumquati tempori tatiae pre sint velecea simpor</p>
  </div>
  <div class="bullets-panel">
    <h2>BULLET<br>POINTS HEAD</h2>
    <ul>
      <li>Tem ellabor emolupid qui restiaes velese</li>
      <li>volum sim qui alita dolupta culluptae consequunte nobitem porectur?</li>
      <li>Ilianda erferia spicimp erferis event la dolendem et am</li>
      <li>quid quia dolorpo remqui ut ommoluptatio excero con porehen dandeliti aut et</li>
      <li>volum sim qui alita dolupta culluptae consequunte nobitem porectur?</li>
      <li>Ilianda erferia spicimp erferis event la dolende</li>
    </ul>
  </div>
  <svg class="abs" style="left:0;top:0" width="408" height="140" viewBox="0 0 408 140">
    <path d="M150 0C220 60 300 104 408 100V0Z" fill="#fff"/>
    <path d="M150 0C220 60 300 104 408 100V112C296 116 214 68 142 0Z" fill="#9a9a9a"/>
    <path d="M142 0C214 68 296 116 408 112V118C292 122 206 72 134 0Z" fill="#dcdcdc"/>
  </svg>
  <div class="logo" style="left:272px;top:26px;width:128px">
    <div class="name">Oakmere Homes</div>
    <div class="tag">Real Estate Center</div>
  </div>
</section>

</body>
</html>
```